The dental corner of brindlewood web page

website for dental office
Already have domain, mostly information only with address, telephone and google map and hours of operation on top. mobile friendly. SEO a most.

Target Market(s)

Local families

Industry/Entity Type

Dental Clinic

Number of Pages Required

1 page

Font styles to use
Serif

Colors

Designer to choose colors to be used in the design.

Requirements
Must have
• SEO
• Information to find the location
• mobile friendly
• dr's. biography
• services offered
• contect to social media (google, facebook, and instagram)
• Se habla espaƱol
• All insurance accepted
• request an appointment form to notify us

```html
<!DOCTYPE html>
<html lang="en">
<head>
<meta charset="utf-8">
<title>The Dental Corner of Brindlewood</title>
<link href="https://fonts.googleapis.com/css2?family=Bodoni+Moda:wght@400;500&family=PT+Serif:wght@400;700&family=Great+Vibes&display=swap" rel="stylesheet">
<style>
:root{
  --blue:#0c5fb8;
  --blue-deep:#0a4ea6;
  --green:#76b82a;
  --ink:#222a33;
  --text:#6a6f75;
  --pale:#eef2f6;
  --paler:#f7f8fa;
  --white:#ffffff;
}
*{box-sizing:border-box;margin:0;padding:0}
html,body{width:1200px;height:3273px;overflow:hidden;background:var(--white)}
body{position:relative;font-family:"PT Serif",Georgia,serif;color:var(--text)}
.display{font-family:"Bodoni Moda","Didot",serif;font-weight:400}
.btn{position:absolute;background:var(--green);color:var(--white);font-family:"PT Serif",serif;font-weight:700;font-size:15px;border-radius:22px;height:38px;line-height:38px;text-align:center;width:132px}

/* hero */
.hero{position:absolute;left:0;top:0;width:1200px;height:600px;background:linear-gradient(100deg,#1a6bc7 0%,#2f82d8 45%,#1565c0 100%)}
.hero-scene{position:absolute;left:0;top:0;width:1200px;height:600px;background:radial-gradient(ellipse at 75% 40%,rgba(120,180,240,.45),transparent 60%)}
.hero-portrait{position:absolute;left:92px;top:112px;width:430px;height:478px;background:linear-gradient(180deg,#9a7a5e 0%,#e8dfd6 55%,#f4f4f4 100%);border-radius:200px 200px 0 0}
.topbar{position:absolute;top:18px;right:180px;font-size:10.5px;color:var(--white);display:flex;gap:12px;align-items:center;white-space:nowrap}
.topbar span{display:flex;align-items:center;gap:5px}
.social{position:absolute;top:14px;left:1042px;display:flex;gap:10px}
.social i{display:block;width:13px;height:13px;background:var(--green);border-radius:2px}
.brand{position:absolute;left:94px;top:26px;width:132px;height:87px;background:var(--white);box-shadow:0 2px 6px rgba(0,0,0,.2);display:flex;flex-direction:column;align-items:center;justify-content:center;gap:6px;padding:6px}
.brand .dot{width:32px;height:32px;border-radius:50%;background:var(--blue)}
.brand p{font-size:10px;line-height:12px;color:var(--blue);font-weight:700;text-align:center}
.nav{position:absolute;left:226px;top:52px;width:880px;height:40px;background:var(--white);display:flex;justify-content:flex-end;align-items:center;gap:44px;padding-right:28px;font-size:13px;color:var(--ink)}
.hero h1{position:absolute;left:600px;top:222px;font-size:72px;line-height:96px;color:var(--white);font-weight:400}
.hero .lead{position:absolute;left:602px;top:322px;width:450px;font-size:13px;line-height:20px;color:var(--white)}
.dots{position:absolute;left:1097px;top:276px;display:flex;flex-direction:column;gap:12px}
.dots i{width:9px;height:9px;border-radius:50%;background:#8fc0ee}
.dots i:first-child{background:var(--green)}
.wave{position:absolute;left:0;top:470px}

/* services */
.services h2{position:absolute;left:94px;top:706px;font-size:42px;line-height:56px;color:var(--ink)}
h2 .accent{color:var(--blue)}
.services .intro{position:absolute;left:94px;top:772px;width:236px;font-size:12.5px;line-height:19px}
.tooth{position:absolute;left:128px;top:920px;width:170px;height:230px;border-radius:60px 60px 30px 30px;background:radial-gradient(ellipse at 40% 35%,#ffffff,#d6dade 80%)}
.tiles{position:absolute;left:367px;top:720px;display:grid;grid-template-columns:repeat(3,242px);grid-template-rows:repeat(2,214px);gap:4px 5px}
.tile{position:relative;border-radius:3px;overflow:hidden}
.tile:nth-child(1){background:linear-gradient(135deg,#1d4f8e,#c9a48d)}
.tile:nth-child(2){background:linear-gradient(135deg,#9aa6ad,#dfe4e6)}
.tile:nth-child(3){background:linear-gradient(135deg,#6d5a4e,#c8b8a8)}
.tile:nth-child(4){background:linear-gradient(135deg,#5a5650,#b9b2a8)}
.tile:nth-child(5){background:linear-gradient(135deg,#2d7a4b,#a8d4b5)}
.tile:nth-child(6){background:linear-gradient(135deg,#1e3350,#6b8fb5)}
.tile span{position:absolute;left:18px;bottom:18px;color:var(--white);font-family:"Bodoni Moda",serif;font-size:18px}
.tile svg{position:absolute;right:14px;bottom:12px}

/* about */
.about{position:absolute;left:0;top:1283px;width:1200px;height:458px;background:var(--pale)}
.about-photo{position:absolute;left:94px;top:76px;width:445px;height:304px;background:linear-gradient(180deg,#8b6b52,#e9e5e1 60%,#f3f3f3)}
.about-mark{position:absolute;left:760px;top:80px;width:300px;height:300px;border-radius:50%;border:14px solid rgba(200,206,214,.45)}
.about h2{position:absolute;left:609px;top:112px;font-size:40px;line-height:54px;color:var(--ink)}
.about p{position:absolute;left:610px;top:180px;width:500px;font-size:12px;line-height:20px}

/* blog */
.blog{position:absolute;left:0;top:1741px;width:1200px;height:583px;background:var(--paler)}
.blog h2{position:absolute;left:0;width:1200px;text-align:center;top:115px;font-size:40px;line-height:54px;color:var(--ink)}
.blog .sub{position:absolute;left:0;width:1200px;text-align:center;top:180px;font-size:12.5px}
.post-img{position:absolute;top:251px;width:249px;height:197px;background:linear-gradient(135deg,#7e8b96,#d9dfe4);box-shadow:0 14px 12px -10px rgba(12,95,184,.35)}
.post{position:absolute;top:251px;width:200px}
.post .date{display:inline-block;background:var(--blue);color:var(--white);font-size:10px;padding:2px 16px;border-radius:10px}
.post h3{font-family:"Bodoni Moda",serif;font-weight:400;font-size:19px;color:var(--ink);margin:8px 0 10px}
.post p{font-size:12.5px;line-height:20px}
.post .btn{position:relative;display:block;margin-top:14px;width:112px;height:34px;line-height:34px;font-size:14px}
.arrow-l{position:absolute;left:94px;top:310px;width:44px;height:98px;background:var(--white);display:flex;align-items:center;justify-content:center}
.arrow-r{position:absolute;left:1062px;top:310px;width:44px;height:98px;background:var(--blue);display:flex;align-items:center;justify-content:center}

/* testimonials */
.testi{position:absolute;left:0;top:2324px;width:1200px;height:524px;background:var(--pale)}
.testi-box{position:absolute;left:209px;top:131px;width:782px;height:286px;background:var(--blue-deep)}
.testi h2{position:absolute;left:0;width:640px;text-align:center;top:36px;font-size:38px;line-height:50px;color:var(--white)}
.testi h2 .g{color:var(--green)}
.quote{position:absolute;left:290px;top:92px;font-family:"Bodoni Moda",serif;font-size:90px;color:rgba(255,255,255,.12);line-height:1}
.testi-text{position:absolute;left:100px;top:122px;width:440px;text-align:center;color:var(--white);font-size:12.5px;line-height:20px}
.sign{position:absolute;left:0;width:640px;text-align:center;top:200px;font-family:"Great Vibes",cursive;font-size:26px;line-height:34px;color:var(--white)}
.role{position:absolute;left:0;width:640px;text-align:center;top:240px;font-size:12px;color:var(--white)}
.pic{position:absolute;background:var(--white);padding:8px;box-shadow:0 4px 10px rgba(0,0,0,.25)}
.pic div{width:100%;height:100%}
.circ{position:absolute;top:255px;width:42px;height:42px;border-radius:50%;background:var(--blue);display:flex;align-items:center;justify-content:center}

/* footer */
.footer{position:absolute;left:0;top:2848px;width:1200px;height:425px}
.footer h4{position:absolute;font-weight:700;font-size:14px;color:var(--ink)}
.footer .col{position:absolute;font-size:12.5px;line-height:30px}
.foot-mark{position:absolute;left:-40px;top:250px;width:260px;height:260px;border-radius:50%;border:18px solid rgba(220,224,229,.6)}
.foot-brand{position:absolute;left:110px;top:198px;display:flex;align-items:center;gap:6px;font-size:11px;font-weight:700;color:var(--blue);width:180px;line-height:13px}
.foot-brand i{flex:none;width:24px;height:24px;border-radius:50%;background:var(--blue)}
.copy{position:absolute;left:0;width:640px;text-align:center;top:350px;font-size:12px;color:var(--ink);white-space:nowrap}
.copy b{color:var(--blue);font-weight:400}
.touch{position:absolute;left:640px;top:0;width:560px;height:425px;background:var(--green)}
.touch .ghost{position:absolute;left:80px;top:80px;font-family:"Bodoni Moda",serif;font-size:44px;color:rgba(255,255,255,.18)}
.touch h4{left:42px;top:104px;color:var(--white)}
.field{position:absolute;left:50px;width:415px;border-bottom:1px solid rgba(255,255,255,.75);font-size:12px;color:var(--white);padding-bottom:8px}
.send{position:absolute;left:444px;top:310px}
</style>
</head>
<body>

<header class="hero">
  <div class="hero-scene"></div>
  <div class="hero-portrait" role="img" aria-label="Portrait of the dentist in a white coat"></div>
  <div class="topbar">
    <span><svg width="10" height="12" viewBox="0 0 10 12"><path d="M5 0a4 4 0 0 1 4 4c0 3-4 8-4 8S1 7 1 4a4 4 0 0 1 4-4z" fill="#76b82a"/></svg>41 Brindle Way, Suite 200</span>
    <span>|</span>
    <span><svg width="11" height="11" viewBox="0 0 11 11"><circle cx="5.5" cy="5.5" r="4.5" fill="none" stroke="#76b82a" stroke-width="1.3"/><path d="M5.5 3v3h2" stroke="#76b82a" fill="none"/></svg>Monday - Saturday 9:00 to 5:00, Sunday 9:30 to 3:00</span>
    <span>|</span>
    <span><svg width="11" height="11" viewBox="0 0 11 11"><path d="M2 1l2 2-1 2a6 6 0 0 0 3 3l2-1 2 2-1 1.5C5 10 1 6 .5 2z" fill="#76b82a"/></svg>(555) 014-2290</span>
  </div>
  <div class="social"><i></i><i></i><i></i></div>
  <div class="brand"><span class="dot"></span><p>The Dental Corner of Brindlewood</p></div>
  <nav class="nav"><span>About</span><span>Mobile Friendly</span><span>Dr's. Biography</span><span>Services</span><span>Contact Us</span></nav>
  <h1 class="display">Dental Clinic</h1>
  <p class="lead">Lorem ipsum dolor sit amet, consectetur adipiscing elit. Donec condimentum nec sem sit amet tincidunt.</p>
  <span class="btn" style="left:600px;top:393px">Read More</span>
  <div class="dots"><i></i><i></i><i></i></div>
  <svg class="wave" width="1200" height="130" viewBox="0 0 1200 130" preserveAspectRatio="none">
    <path d="M0 110 C300 60 650 40 900 70 C1020 85 1120 70 1200 40 L1200 130 L0 130Z" fill="#ffffff"/>
  </svg>
</header>

<section class="services">
  <h2 class="display"><span class="accent">Our</span> Services</h2>
  <p class="intro">Lorem ipsum dolor sit amet, consectetur adipiscing elit. Donec condimentum nec sem sit amet tincidunt.</p>
  <span class="btn" style="left:94px;top:860px">Read More</span>
  <div class="tooth" role="img" aria-label="White tooth illustration"></div>
  <div class="tiles">
    <div class="tile" role="img" aria-label="Patient receiving a dental cleaning"><span>Lorem Ipsum</span><svg width="32" height="32"><circle cx="16" cy="16" r="16" fill="#76b82a"/><path d="M13 10l6 6-6 6" stroke="#fff" stroke-width="2.5" fill="none"/></svg></div>
    <div class="tile" role="img" aria-label="Clinic corridor"><span>Lorem Ipsum</span><svg width="32" height="32"><circle cx="16" cy="16" r="16" fill="#76b82a"/><path d="M13 10l6 6-6 6" stroke="#fff" stroke-width="2.5" fill="none"/></svg></div>
    <div class="tile" role="img" aria-label="Dental examination"><span>Lorem Ipsum</span><svg width="32" height="32"><circle cx="16" cy="16" r="16" fill="#76b82a"/><path d="M13 10l6 6-6 6" stroke="#fff" stroke-width="2.5" fill="none"/></svg></div>
    <div class="tile" role="img" aria-label="Dental chair equipment"><span>Lorem Ipsum</span><svg width="32" height="32"><circle cx="16" cy="16" r="16" fill="#76b82a"/><path d="M13 10l6 6-6 6" stroke="#fff" stroke-width="2.5" fill="none"/></svg></div>
    <div class="tile" role="img" aria-label="Treatment room"><span>Lorem Ipsum</span><svg width="32" height="32"><circle cx="16" cy="16" r="16" fill="#76b82a"/><path d="M13 10l6 6-6 6" stroke="#fff" stroke-width="2.5" fill="none"/></svg></div>
    <div class="tile" role="img" aria-label="Dental surgery under lights"><span>Lorem Ipsum</span><svg width="32" height="32"><circle cx="16" cy="16" r="16" fill="#76b82a"/><path d="M13 10l6 6-6 6" stroke="#fff" stroke-width="2.5" fill="none"/></svg></div>
  </div>
</section>

<section class="about">
  <div class="about-photo" role="img" aria-label="Portrait of the dentist"></div>
  <div class="about-mark"></div>
  <h2 class="display"><span class="accent">About</span> Myself</h2>
  <p>Lorem ipsum dolor sit amet, consectetur adipiscing elit. Donec condimentum nec sem sit amet tincidunt. Cras sagittis sapien purus, at lobortis eros tempus eget. Aenean consectetur vel tortor viverra aliquet. Aenean facilisis metus ut laoreet tempus. Fusce tincidunt tellus vel finibus varius. Nulla vel risus nunc. Vestibulum tempus bibendum mollis.</p>
  <span class="btn" style="left:610px;top:300px">Read More</span>
</section>

<section class="blog">
  <h2 class="display"><span class="accent">Latest</span> Blog</h2>
  <p class="sub">Lorem ipsum dolor sit amet, consectetur adipiscing elit. Donec condimentum nec sem sit amet tincidunt.</p>
  <div class="post-img" style="left:94px" role="img" aria-label="Dental instruments on a tray"></div>
  <article class="post" style="left:371px"><span class="date">Oct, 01 2018</span><h3>Lorem Ipsum</h3><p>Lorem ipsum dolor sit amet, consectetur adipiscing elit. Donec condimentum nec sem sit amet tincidunt. Cras sagittis sapien purus, at lobortis eros tempus</p><span class="btn">Learn More</span></article>
  <div class="post-img" style="left:646px" role="img" aria-label="Dental instruments on a tray"></div>
  <article class="post" style="left:918px;width:144px;overflow:hidden"><span class="date">Oct, 01 2018</span><h3>Lorem Ipsum</h3><p style="width:200px">Lorem ipsum dolor sit amet, consectetur adipiscing elit. Donec condimentum nec sem sit amet tincidunt. Cras sagittis sapien purus, at lobortis eros tempus</p><span class="btn">Learn More</span></article>
  <div class="arrow-l"><svg width="18" height="50"><path d="M16 2L3 25l13 23" stroke="#222a33" stroke-width="2" fill="none"/></svg></div>
  <div class="arrow-r"><svg width="18" height="50"><path d="M2 2l13 23L2 48" stroke="#fff" stroke-width="2" fill="none"/></svg></div>
</section>

<section class="testi">
  <div class="testi-box">
    <h2 class="display"><span class="g">Client</span> Testimonials</h2>
    <div class="quote">&ldquo;</div>
    <p class="testi-text">Lorem ipsum dolor sit amet, consectetur adipiscing elit. Donec condimentum nec sem sit amet tincidunt. Cras sagittis sapien purus, at lobortis eros tempus eget. Aenean consectetur vel tortor viverra aliquet.</p>
    <p class="sign">-Lorem Ipsum</p>
    <p class="role">Simply Dummy</p>
  </div>
  <div class="pic" style="left:935px;top:80px;width:170px;height:180px;transform:rotate(14deg)"><div role="img" aria-label="Close-up of a healthy smile" style="background:linear-gradient(135deg,#d95b5b,#f3e6e0)"></div></div>
  <div class="pic" style="left:815px;top:90px;width:165px;height:185px;transform:rotate(-14deg)"><div role="img" aria-label="Smiling client" style="background:linear-gradient(180deg,#d9c3a0,#f1f1f1)"></div></div>
  <div class="circ" style="left:94px"><svg width="14" height="14"><path d="M10 1L4 7l6 6" stroke="#fff" stroke-width="2" fill="none"/></svg></div>
  <div class="circ" style="left:1064px"><svg width="14" height="14"><path d="M4 1l6 6-6 6" stroke="#fff" stroke-width="2" fill="none"/></svg></div>
</section>

<footer class="footer">
  <div class="foot-mark"></div>
  <h4 style="left:94px;top:105px">About Me</h4>
  <p class="col" style="left:94px;top:126px;width:170px;line-height:21px">Lorem ipsum dolor sit amet, consectetur adipiscing elit. Donec condimentum nec</p>
  <div class="foot-brand"><i></i>The Dental Corner of Brindlewood</div>
  <h4 style="left:347px;top:105px">Services</h4>
  <p class="col" style="left:347px;top:132px">Lorem ipsum<br>Dolor sit amet<br>Consectetur<br>adipiscing elit</p>
  <p class="col" style="left:478px;top:132px">Lorem ipsum<br>Dolor sit amet<br>Consectetur<br>adipiscing elit</p>
  <p class="copy">&copy; 2018 <b>The Dental Corner of Brindlewood</b>. All Right Reserved.</p>
  <div class="touch">
    <div class="ghost">Get In Touch</div>
    <h4>Get In Touch</h4>
    <div class="field" style="top:150px">Name</div>
    <div class="field" style="top:192px">Email</div>
    <div class="field" style="top:228px;height:70px">Message</div>
    <svg class="send" width="20" height="16" viewBox="0 0 20 16"><path d="M0 0l20 8L0 16l3-8z" fill="#fff"/></svg>
  </div>
</footer>

</body>
</html>
```